"Bright Pathways" needs a business card design

we would like our logo and slogan with
Business name- Bright Pathways Pty Ltd
Managing Director - Morgan Tully - 0471625830
Address - 14 Wattlebend Court Kelmore Park WA 6140
Email - brightpathways@mailnest.com.au
Website - www.brightpathways-example.com.au
ABN - 83902417566

We would like the colours as the logo to be used or as close as possible

```html
<!DOCTYPE html>
<html lang="en">
<head>
<meta charset="utf-8">
<title>Bright Pathways – Business Card</title>
<link rel="stylesheet" href="https://fonts.googleapis.com/css2?family=Montserrat:wght@400;600;700&family=Questrial&family=Source+Sans+3:wght@400;600&display=swap">
<style>
  :root {
    --page-bg: #ece8e1;
    --card-white: #ffffff;
    --brand-brown: #6b4424;
    --brand-orange: #f0901e;
    --brand-green: #8cc63f;
    --green-rule: #74ad2c;
    --text-light: #ffffff;
  }
  * { box-sizing: border-box; margin: 0; padding: 0; }
  html, body { width: 1200px; height: 753px; overflow: hidden; background: var(--page-bg); }
  .card {
    position: absolute; left: 120px; top: 98px; width: 960px; height: 556px;
    background: var(--card-white); overflow: hidden;
    box-shadow: 0 6px 22px rgba(0,0,0,.18);
  }
  .brand {
    position: absolute; left: 40px; top: 430px; width: 460px;
  }
  .brand-mark {
    display: flex; align-items: center; gap: 14px;
  }
  .brand-dot { width: 34px; height: 34px; border-radius: 50%; background: var(--brand-orange); flex: none; }
  .brand-name {
    font-family: "Source Sans 3", sans-serif; font-weight: 600; font-size: 46px;
    letter-spacing: .5px; color: var(--brand-brown); white-space: nowrap; line-height: 1;
  }
  .brand-slogan {
    font-family: "Source Sans 3", sans-serif; font-size: 15px; color: var(--brand-brown);
    text-align: right; margin-top: 6px; padding-right: 20px;
  }
  .holder { position: absolute; left: 520px; top: 62px; }
  .holder-role { font-family: "Questrial", sans-serif; font-size: 26px; color: var(--brand-orange); }
  .holder-role b { font-family: "Montserrat", sans-serif; font-weight: 600; }
  .holder-name { font-family: "Questrial", sans-serif; font-size: 50px; color: var(--brand-brown); line-height: 1.05; white-space: nowrap; }
  .holder-name b { font-family: "Montserrat", sans-serif; font-weight: 700; }
  .brown-band { position: absolute; left: 505px; top: 196px; width: 455px; height: 10px; background: var(--brand-brown); }
  .contact-panel {
    position: absolute; left: 520px; top: 214px; width: 440px; height: 342px;
    background: var(--brand-green); padding: 14px 20px 0 22px; color: var(--text-light);
    font-family: "Questrial", sans-serif;
  }
  .contact-row {
    display: flex; align-items: center; gap: 14px; border-bottom: 4px solid var(--green-rule);
    padding: 8px 0;
  }
  .contact-row:last-child { border-bottom: none; }
  .contact-icon { width: 32px; height: 32px; flex: none; }
  .phone { font-size: 28px; }
  .phone b, .address b, .email b, .web b, .abn b { font-family: "Montserrat", sans-serif; font-weight: 700; }
  .address { font-size: 19px; line-height: 1.2; }
  .address b { font-size: 22px; }
  .email { font-size: 18px; }
  .web { font-size: 17px; white-space: nowrap; }
  .abn { font-size: 24px; padding-left: 46px; }
  .abn b { font-size: 22px; margin-right: 12px; }
</style>
</head>
<body>
<div class="card">
  <div class="brand">
    <div class="brand-mark">
      <span class="brand-dot"></span>
      <span class="brand-name">BRIGHT PATHWAYS</span>
    </div>
    <p class="brand-slogan">Support, Growth, Independence</p>
  </div>

  <div class="holder">
    <p class="holder-role">Managing <b>Director</b></p>
    <p class="holder-name"><b>MORGAN</b> TULLY</p>
  </div>

  <div class="brown-band"></div>

  <div class="contact-panel">
    <div class="contact-row">
      <svg class="contact-icon" viewBox="0 0 32 32" fill="none" stroke="#fff" stroke-width="2"><circle cx="16" cy="16" r="14"/><path d="M11 9l3 0 1.5 4-2 1.5c1 2.2 2.8 4 5 5l1.5-2 4 1.5v3c-7 .5-13.5-6-13-13z" fill="#fff" stroke="none"/></svg>
      <p class="phone">0471 <b>625 830</b></p>
    </div>
    <div class="contact-row">
      <svg class="contact-icon" viewBox="0 0 32 32"><path d="M16 2a10 10 0 0 0-10 10c0 7 10 18 10 18s10-11 10-18A10 10 0 0 0 16 2z" fill="#fff"/><circle cx="16" cy="12" r="4" fill="#8cc63f"/></svg>
      <p class="address"><b>14 Wattlebend Court</b><br>Kelmore Park WA 6140</p>
    </div>
    <div class="contact-row">
      <svg class="contact-icon" viewBox="0 0 32 32" fill="none" stroke="#fff" stroke-width="2"><circle cx="16" cy="16" r="14"/><rect x="9" y="11" width="14" height="10"/><path d="M9 11l7 6 7-6"/></svg>
      <p class="email"><b>brightpathways</b>@mailnest.com.au</p>
    </div>
    <div class="contact-row">
      <svg class="contact-icon" viewBox="0 0 32 32" fill="none" stroke="#fff" stroke-width="2"><circle cx="16" cy="16" r="13"/><ellipse cx="16" cy="16" rx="6" ry="13"/><path d="M3 16h26M5 9h22M5 23h22"/></svg>
      <p class="web">www.<b>BRIGHTPATHWAYS</b>-example.com.au</p>
    </div>
    <div class="contact-row">
      <p class="abn"><b>ABN</b>83902417566</p>
    </div>
  </div>
</div>
</body>
</html>
```